Rodeo Sponsor booklet

I am needing a multi page handout made for potential sponsors for our Tamsley Flats Rodeo. I have attached our previous one and our 2025 poster that we would like it to flow similarly. You will see on the "example of 2025" the markup we would like changed and of course new front cover etc.
These are the following uploads
2025 Tamsley Flats Rodeo -5.jpg this is the new 2025 poster match look and feel
Rodeo Brochure R-3.pdf. this is 2024 sponsor brochure I need the same idea with a different look and feel but match the above poster
This is the new information that is needed on the new 2025 brochure with changes that I would like made. it can have what ever look and feel I was just playing around. nothing about it needs to be similar to this but all information does need to be in the document
The rest are photos we like and you can use which ever I just like the look and feel of the 2024 one so want that same feeling!

```html
<!DOCTYPE html>
<html lang="en">
<head>
<meta charset="utf-8">
<title>Tamsley Flats Rodeo – Sponsor Booklet</title>
<link rel="stylesheet" href="https://fonts.googleapis.com/css2?family=Righteous&family=Fjalla+One&family=Josefin+Sans:wght@300;400&display=swap">
<style>
  :root{
    --backdrop:#a8a8a8;
    --sun-top:#f7c55c;
    --sun-bottom:#e4892b;
    --ink:#3a3835;
    --tag:#efa12f;
    --paper:#ffffff;
    --rule:#4a4a4a;
  }
  *{box-sizing:border-box;margin:0;padding:0}
  html,body{width:857px;height:1200px;overflow:hidden}
  body{background:var(--backdrop);position:relative;font-family:"Josefin Sans",sans-serif;color:var(--ink)}

  .page{position:absolute;width:370px;height:522px;overflow:hidden}
  .page--sun{background:linear-gradient(180deg,var(--sun-top) 0%,var(--sun-bottom) 100%)}
  .page--cover{left:244px;top:69px}
  .page--letter{left:41px;top:621px}
  .page--levels{left:447px;top:621px;background:var(--paper)}

  /* cover */
  .cover__title{position:absolute;top:28px;left:0;width:100%;text-align:center;font-family:"Righteous",sans-serif;font-size:66px;letter-spacing:2px;line-height:1}
  .cover__subtitle{position:absolute;top:104px;left:0;width:100%;text-align:center;font-family:"Righteous",sans-serif;font-size:24px;letter-spacing:2px;line-height:1}
  .cover__art{position:absolute;left:50px;top:136px;width:270px;height:262px;border-radius:50%;
    background:radial-gradient(circle,rgba(58,56,53,.55) 0%,rgba(58,56,53,.25) 45%,rgba(58,56,53,0) 72%)}
  .cover__date{position:absolute;top:404px;left:0;width:100%;text-align:center;font-family:"Fjalla One",sans-serif;font-size:31px;line-height:1;transform:scaleX(.9)}
  .cover__host{position:absolute;top:445px;left:0;width:100%;text-align:center;font-size:28px;font-weight:300;line-height:1}
  .cover__motto{position:absolute;top:480px;left:0;width:100%;text-align:center;font-size:12px;font-weight:300}

  /* letter */
  .letter{position:absolute;left:21px;top:60px;width:330px;font-size:6.6px;line-height:9px;font-weight:300;text-align:justify}
  .letter p{margin-bottom:8px}

  /* sponsorship levels */
  .levels__heading{position:absolute;left:20px;top:28px;font-family:"Righteous",sans-serif;font-size:20px;font-weight:400;letter-spacing:1.5px}
  .tier{position:absolute;border:1px solid var(--rule);padding:7px 9px}
  .tier__name{font-size:12px;line-height:15px;width:70px;font-weight:300}
  .tier__price{position:absolute;top:4px;right:-1px;background:var(--tag);font-size:23px;font-weight:300;line-height:33px;padding:0 8px;width:82px;text-align:center}
  .tier__perks{margin-top:14px;font-size:6.4px;line-height:9px;font-weight:300;list-style:none}
  .tier--bronze{left:17px;top:82px;width:169px;height:113px}
  .tier--silver{left:185px;top:82px;width:169px;height:113px}
  .tier--gold{left:17px;top:215px;width:169px;height:113px}
  .tier--platinum{left:185px;top:215px;width:169px;height:113px}
  .tier--diamond{left:17px;top:344px;width:246px;height:127px}
  .levels__horseshoe{position:absolute;left:250px;top:357px;width:120px;height:165px;
    background:linear-gradient(150deg,rgba(58,56,53,.35),rgba(58,56,53,.1));border-radius:60px 0 0 0}
</style>
</head>
<body>

<section class="page page--sun page--cover">
  <h1 class="cover__title">RODEO</h1>
  <div class="cover__subtitle">TAMSLEY</div>
  <div class="cover__art" role="img" aria-label="Illustration of a jockey riding a galloping horse over a burst of lines"></div>
  <div class="cover__date">1,2,3 AUG 2025</div>
  <div class="cover__host">Tamsley Flats Community</div>
  <div class="cover__motto">"Ride hard, shoot straight, and speak the truth."</div>
</section>

<section class="page page--sun page--letter">
  <div class="letter">
    <p>Dear Valued Sponsor,</p>
    <p>I hope this letter finds you well.</p>
    <p>As we reflect on the incredible success of the 2024 Tamsley Flats Rodeo, we are filled with gratitude and excitement. Each year, our event continues to grow, and thanks to the support of our sponsors, we are proud to uphold a 36-year tradition that brings together cowboys, cowgirls, and rodeo fans from across the region.</p>
    <p>We are thrilled to announce that 2025 will be a landmark year for the Tamsley Flats Rodeo! Not only are we planning another action-packed rodeo season, but we are also working on the construction of our new rodeo arena, set to open in 2026. This state-of-the-art facility, located just north of our community, will feature top-tier rodeo equipment, new buildings, offices, announcer booths, and more—enhancing the experience for both contestants and spectators.</p>
    <p>The 2025 Tamsley Flats Rodeo will continue its tradition of two thrilling, one-day events, where contestants have a chance to win a custom buckle each day. Additionally, we are excited to introduce a custom Tamsley Drum for the Average winner, adding a unique and meaningful prize to our event.</p>
    <p>This year, we're bringing even more excitement with the return of the Mini Wild Pony Race, along with fantastic entertainment featuring Dusty Timber. Our substantial payout remains a major draw, ensuring a high level of competition and attracting a larger and more diverse group of skilled participants.</p>
    <p>Your sponsorship is more than just a contribution—it's an investment in the future of rodeo and a commitment to preserving an important community tradition. Funds raised will support critical needs, including ground upgrades, rodeo stock, event payouts, prizes, and essential supplies.</p>
    <p>Enclosed, you'll find our 2025 sponsorship levels for your consideration. This year, we've made contributions even more convenient with multiple payment options, including Electronic Funds Transfer (EFT), e-Transfer, credit card, debit, or cheque. All payments must be sent to 4120 Ridgeway Rd, Tamsley Flats, BC V0X 2K4. Please complete one of the attached forms at your earliest convenience.</p>
    <p>If you have any questions or need further details, please don't hesitate to reach out. Together, let's make the 2025 Tamsley Flats Rodeo an unforgettable event that continues to honor the rich heritage and spirit of our community.</p>
    <p>We look forward to seeing you there!</p>
    <p>Sincerely,<br>Marla Kettering<br>Tamsley Flats Rodeo Manager</p>
    <p>"A rodeo is not just an event; it's a way of life. It's where courage meets determination, where tradition meets competition, and where a community comes together. Thank you for being part of our rodeo family."</p>
  </div>
</section>

<section class="page page--levels">
  <h2 class="levels__heading">BASE SPONSORSHP LEVELS</h2>

  <article class="tier tier--bronze">
    <h3 class="tier__name">Bronze Supporter</h3>
    <div class="tier__price">$1500</div>
    <ul class="tier__perks">
      <li>Company name listed in the event program.</li>
      <li>Social media mention on all rodeo related pages.</li>
      <li>Small logo display on the event's main digital screen.</li>
      <li>4 Single Day Passes to the rodeo.</li>
    </ul>
  </article>

  <article class="tier tier--silver">
    <h3 class="tier__name">Silver Supporter</h3>
    <div class="tier__price">$3000</div>
    <ul class="tier__perks">
      <li>Includes all Bronze Supporter benefits.</li>
      <li>Company logo on the event website.</li>
      <li>Company banner displayed at the event (provided by the rodeo).</li>
      <li>8 Single Day Passes to the rodeo.</li>
    </ul>
  </article>

  <article class="tier tier--gold">
    <h3 class="tier__name">Gold Supporter</h3>
    <div class="tier__price">$5000</div>
    <ul class="tier__perks">
      <li>Includes all Silver Sponsor benefits.</li>
      <li>Medium-sized banner at the event (provided by the rodeo).</li>
      <li>6 Weekend Passes to the rodeo.</li>
    </ul>
  </article>

  <article class="tier tier--platinum">
    <h3 class="tier__name">Platinum Supporter</h3>
    <div class="tier__price">$6500</div>
    <ul class="tier__perks">
      <li>Includes all Bronze Supporter benefits.</li>
      <li>Company logo on the event website.</li>
      <li>Company banner displayed at the event (provided by the rodeo).</li>
      <li>10 weekend passes with VIP seating to the rodeo.</li>
    </ul>
  </article>

  <article class="tier tier--diamond">
    <h3 class="tier__name">Diamond Supporter</h3>
    <div class="tier__price">$8500</div>
    <ul class="tier__perks">
      <li>Includes all Platinum Contributor benefits.</li>
      <li>Large banner in a prime location at the event (provided by the rodeo).</li>
      <li>Exclusive 2 VIP parking spots.</li>
      <li>12 Weekend VIP Passes to the Rodeo.</li>
      <li>Option to provide short Commercial for your company.</li>
      <li>Option to provide short Commercial for your company.</li>
      <li>A banner on one of the 6 chutes or main gates used in the arena.</li>
    </ul>
  </article>

  <div class="levels__horseshoe" role="img" aria-label="Illustration of a horseshoe"></div>
</section>

</body>
</html>
```